Commercial janitorial cleaning

Janitorial cleaning particularly for commercial buildings. Website needs to specify free estimates. Location of service is Hudson, Valatie, East Greenbush, Troy, Albany ny area. Services page with Janitorial services- General Office Cleaning, Construction Cleaning, Carpet Extraction, Consultation/Business, Lighting Maintenance, Seasonal Deep Cleaning, Window cleaning, Event Cleaning, Floor and Carpet Cleaning, Floor Striping and Waxing. Contact us page with email phone number on page and a request page that emails me if they have any questions. About us page-the picture of my family on it with a section I can type a story myself.

Target Market(s)

Commercial businesses

Industry/Entity Type

Janitorial Service

Number of Pages Required

4 page

Font styles to use
Serif
Sans Serif
Script

Colors
ec1f27
1b1b1b
ffffff
9d9d9d

Requirements
Must have
• Phone number 555-314-2760. Must have free estimates on home page. Going for industrial / modern look to website
Nice to have
• Logo is a red and black building so if those colors could be coordinated to website that would be awesome.

```html
<!DOCTYPE html>
<html lang="en">
<head>
<meta charset="utf-8">
<title>Brightline Cleaning Services – Commercial Janitorial Cleaning</title>
<link rel="stylesheet" href="https://fonts.googleapis.com/css2?family=Poppins:wght@400;500;600;700&display=swap">
<style>
  :root{
    --red:#d2171e;
    --ink:#1b1b1b;
    --white:#ffffff;
    --grey:#9d9d9d;
    --panel:#f0f0f0;
    --gold:#e6cf2a;
    --quote:#d8c41e;
  }
  *{margin:0;padding:0;box-sizing:border-box}
  html,body{width:934px;height:1200px;overflow:hidden}
  body{font-family:"Poppins",sans-serif;color:var(--ink);background:var(--white);position:relative}

  .topbar{height:22px;background:var(--red);color:var(--white);font-size:7px;position:relative}
  .topbar .contact{position:absolute;left:126px;top:0;height:22px;display:flex;align-items:center;gap:18px}
  .topbar .item{display:flex;align-items:center;gap:6px}
  .topbar b{font-weight:600}
  .topbar .quote{position:absolute;left:734px;width:74px;top:0;height:22px;background:var(--quote);color:var(--ink);font-weight:600;font-size:6.5px;display:flex;align-items:center;justify-content:center}

  .header{height:58px;position:relative}
  .brand{position:absolute;left:128px;top:18px;display:flex;align-items:center;gap:7px}
  .brand .mark{width:14px;height:14px;background:var(--red)}
  .brand .name{font-weight:700;font-size:14px;color:var(--ink);letter-spacing:.2px}
  .nav{position:absolute;left:542px;top:22px;display:flex;align-items:center;font-size:9px}
  .nav a{color:var(--ink);text-decoration:none;margin-right:29px}
  .nav a.active{background:var(--red);color:var(--white);width:50px;height:18px;display:flex;align-items:center;justify-content:center;margin-right:17px}
  .nav a:last-child{margin-right:0}

  .hero{height:242px;position:relative;background:linear-gradient(90deg,#eef1f6 0%,#dfe6ef 40%,#e9eef5 100%)}
  .hero .photo{position:absolute;left:0;top:0;width:400px;height:242px;background:linear-gradient(135deg,#e4e9f0 0%,#cdb79c 45%,#f0a52a 80%,#dfe5ee 100%)}
  .hero .banner{position:absolute;left:436px;top:51px;width:372px;height:134px;background:var(--red);padding:14px 16px;color:var(--white)}
  .hero h1{font-weight:700;font-size:19.5px;line-height:26px;text-transform:uppercase;letter-spacing:.2px}
  .hero h1 span{color:var(--gold)}
  .hero p{margin-top:9px;font-size:10.5px;font-weight:500;text-transform:uppercase}

  .section-title{font-weight:700;font-size:14.5px;text-align:center;text-transform:uppercase;letter-spacing:.3px}
  .section-title span{color:var(--red)}
  .divider{position:relative;height:8px;margin:6px auto 0}
  .divider::before{content:"";position:absolute;left:0;right:0;top:4px;height:1px;background:var(--ink)}
  .divider i{position:absolute;left:50%;top:0;width:6px;height:6px;margin-left:-3px;margin-top:1px;background:var(--red);transform:rotate(45deg);outline:6px solid var(--white)}
  .body-text{font-size:8.4px;line-height:15.2px;text-align:center;color:var(--ink)}

  .welcome{height:240px;padding-top:29px}
  .welcome .divider{width:318px}
  .welcome .body-text{width:664px;margin:18px auto 0}
  .btn{width:62px;height:22px;margin:13px auto 0;background:var(--red);color:var(--white);font-size:8.5px;display:flex;align-items:center;justify-content:center}

  .services{height:288px;background:var(--panel);padding-top:24px;position:relative}
  .services .divider{width:102px}
  .services .divider i{outline-color:var(--panel)}
  .services .body-text{margin-top:13px;line-height:14px}
  .services .photo{position:absolute;left:126px;top:121px;width:252px;height:129px;border:5px solid var(--white);background:linear-gradient(120deg,#dbe4ef 0%,#9fd64a 40%,#c58ad0 65%,#e5e9ef 100%)}
  .service-grid{position:absolute;left:414px;top:121px;display:grid;grid-template-columns:125px 124px 125px;grid-auto-rows:35px;column-gap:10px;row-gap:12px}
  .service-grid div{background:var(--white);font-size:8.6px;font-weight:600;display:flex;align-items:center;justify-content:center;text-align:center}
  .service-grid .active{background:var(--red);color:var(--white)}

  .testimonials{height:262px;padding-top:34px;text-align:center}
  .testimonials .divider{width:102px}
  .testimonials .body-text{width:664px;margin:13px auto 0}
  .avatar{width:48px;height:40px;margin:20px auto 0;border:2px solid var(--red);border-radius:4px;background:linear-gradient(160deg,#c9d4de,#e07a3c)}
  .client{margin-top:4px;font-size:10.5px;font-weight:500;letter-spacing:.3px}
  .position{font-size:7px;margin-top:1px}
  .dots{display:flex;justify-content:center;gap:3px;margin-top:11px}
  .dots i{width:5px;height:5px;background:var(--ink)}
  .dots i:first-child{background:var(--red)}

  .footer{position:absolute;left:0;top:1112px;width:934px;height:88px;background:#000;color:var(--white);text-align:center}
  .footer .links{display:flex;justify-content:center;gap:21px;font-size:7.5px;padding-top:14px}
  .footer .rule{width:415px;height:1px;background:#333;margin:8px auto 0}
  .social{display:flex;justify-content:center;gap:3px;margin-top:9px}
  .social i{width:13px;height:13px;background:var(--red)}
  .copy{font-size:7px;margin-top:7px}
</style>
</head>
<body>
  <div class="topbar">
    <div class="contact">
      <div class="item">
        <svg width="8" height="9" viewBox="0 0 10 10"><path d="M2 0.5 L3.6 0.5 L4.4 3 L3.2 4 Q4.2 6 6 6.8 L7 5.6 L9.5 6.4 L9.5 8 Q9.5 9.5 8 9.5 Q1 9 0.5 2 Q0.5 0.5 2 0.5Z" fill="#fff"/></svg>
        <span><b>Call Us :</b> 555-314-2760</span>
      </div>
      <div class="item">
        <svg width="11" height="8" viewBox="0 0 11 8"><rect x="0.5" y="0.5" width="10" height="7" fill="none" stroke="#fff"/><path d="M0.5 0.5 L5.5 4.5 L10.5 0.5" fill="none" stroke="#fff"/></svg>
        <span><b>Email :</b> info@brightlinecleaning.example</span>
      </div>
    </div>
    <div class="quote">GET A FREE QUOTE</div>
  </div>

  <header class="header">
    <div class="brand"><span class="mark"></span><span class="name">BRIGHTLINE CLEANING</span></div>
    <nav class="nav">
      <a class="active" href="#">Home</a>
      <a href="#">About Us</a>
      <a href="#">Our Services</a>
      <a href="#">Contact Us</a>
    </nav>
  </header>

  <section class="hero">
    <div class="photo" role="img" aria-label="Smiling cleaner holding a basket of cleaning supplies"></div>
    <div class="banner">
      <h1>We offer janitorial cleaning<br>particularly for<br><span>commercial buildings</span></h1>
      <p>Serving all of Hudson, Valatie, Troy &amp; Albany</p>
    </div>
  </section>

  <section class="welcome">
    <h2 class="section-title">Welcome to <span>Brightline Cleaning Services</span></h2>
    <div class="divider"><i></i></div>
    <p class="body-text">Our team is a local commercial cleaning crew and it's most commonly hired to tidy and shine busy work floors. A clean office is a space that is typically noticed by the fresh look of every room. Our team is a local commercial cleaning crew and it's most commonly hired to tidy and shine busy work floors. A clean office is a space that is typically noticed by the fresh look of every room. Our team is a local commercial cleaning crew and it's most commonly hired to tidy and shine busy work floors. A clean office is a space that is typically noticed by the fresh look of every room. Our team is a local commercial cleaning crew and it's most commonly hired to tidy and shine busy work floors. A clean office is a space that is typically noticed by the fresh look of every room. Our team is a local commercial cleaning crew and it's most commonly hired to tidy and shine busy work floors. A clean office is a space that is typically noticed by the fresh look of every room. Our team is a local commercial cleaning crew and it's most commonly.</p>
    <a class="btn">Read More</a>
  </section>

  <section class="services">
    <h2 class="section-title">Our <span>Services</span></h2>
    <div class="divider"><i></i></div>
    <p class="body-text">Our team is a local commercial cleaning crew and it's most commonly hired to tidy and shine busy work floors. A clean office is a space that is typically noticed by the.<br>Our team is a local commercial cleaning crew and it's most commonly hired to tidy and shine busy work floors.</p>
    <div class="photo" role="img" aria-label="Basket of spray bottles and microfibre cloths"></div>
    <div class="service-grid">
      <div class="active">General Office Cleaning</div>
      <div>Construction Cleaning</div>
      <div>Carpet Extraction</div>
      <div>Building Maintenance</div>
      <div>Lighting Maintenance</div>
      <div>Seasonal Deep Cleaning</div>
      <div>Window Cleaning</div>
      <div>Event Cleaning</div>
      <div>Floor and Carpet Cleaning</div>
    </div>
  </section>

  <section class="testimonials">
    <h2 class="section-title">Clients <span>Testimonials</span></h2>
    <div class="divider"><i></i></div>
    <p class="body-text">Our team is a local commercial cleaning crew and it's most commonly hired to tidy and shine busy work floors. A clean office is a space that is typically noticed by the fresh look of every room. Our team is a local commercial cleaning crew and it's most commonly hired to tidy and shine busy work floors. A clean office is a space that is typically noticed by the fresh look of every room. Our team is a local commercial cleaning crew and it's most commonly hired to tidy and shine busy work floors.</p>
    <div class="avatar" role="img" aria-label="Client portrait"></div>
    <div class="client">Client name</div>
    <div class="position">position</div>
    <div class="dots"><i></i><i></i><i></i></div>
  </section>

  <footer class="footer">
    <div class="links"><span>Home</span><span>About us</span><span>Services</span><span>Contact Us</span></div>
    <div class="rule"></div>
    <div class="social"><i></i><i></i><i></i><i></i><i></i></div>
    <p class="copy">© 2017 Brightline Cleaning Services. All Rights Reserved.</p>
  </footer>
</body>
</html>
```